Spring Menu Design for newly renovated, vibrant cafe with exciting food

We need a menu designed for our brand new Spring menu. We would like it to be landscape with a number of columns. I'd ideally like it to be two sided - with the front side having the cafe logo - and the rest of the menu on the other side. I do understand there may be too much content to achieve this. We would like greys and soft pinks used - with an easy to understand font, which exudes style and warmth. I have attached a photo of one of the cushions in the cafe. The staff are currently wearing this dusty pink - with grey aprons with black straps. Our logo is attached and includes red, black and grey. I don't want to see red on the menu - except for a discreet heart placed somewhere within the design. Please feel free to contact me for more info. Looking forward to seeing exciting designs

Requirements
Must have
• Clean design
• Blush pink and grey feel
• landscape
Nice to have
• Front side for logo, second side for menu
Should not have
• No frumpy, bulky looks

```html
<!DOCTYPE html>
<html lang="en">
<head>
<meta charset="utf-8">
<title>bloom &amp; crumb café — Spring Menu</title>
<link rel="stylesheet" href="https://fonts.googleapis.com/css2?family=Poppins:wght@400;600;700&family=Oswald:wght@500&display=swap">
<style>
:root{
  --stage:#e7e7e7;
  --paper:#ffffff;
  --ink:#111111;
  --text:#3a3a3a;
  --blush:#f2a7a7;
  --blush-soft:#f6c4c4;
  --pill:#ef7f7f;
  --frame:#f0b4b4;
}
*{margin:0;padding:0;box-sizing:border-box}
html,body{width:814px;height:1200px;overflow:hidden;background:var(--stage)}
body{position:relative;font-family:"Poppins",sans-serif;color:var(--text)}

.sheet{position:absolute;left:28px;width:756px;height:534px;background:var(--paper);box-shadow:0 8px 14px rgba(0,0,0,.22)}
.sheet--front{top:18px;overflow:hidden}
.sheet--back{top:612px}
.side-label{position:absolute;left:0;width:814px;text-align:center;font-family:"Poppins",sans-serif;font-size:21px;font-weight:400;letter-spacing:.5px;color:var(--ink)}
.side-label--front{top:562px}
.side-label--back{top:1158px}

/* front */
.cover-photo{position:absolute;inset:0;background:radial-gradient(ellipse at 40% 45%,#e9dccb 0%,#c9a77e 35%,#8a6a48 70%,#d8d4cf 100%)}
.cover-diamond{position:absolute;inset:0}
.brand{position:absolute;top:246px;left:0;width:756px;text-align:center;white-space:nowrap}
.brand-name{font-family:"Poppins",sans-serif;font-weight:400;font-size:30px;color:#2b2b2b;letter-spacing:-.5px;line-height:1}
.brand-mark{display:inline-block;width:7px;height:7px;border-radius:50%;background:#2b2b2b;margin-left:5px;vertical-align:middle}

/* back */
.back-frame{position:absolute;inset:12px;border:3px solid var(--frame)}
.panel{position:absolute}
.panel--dashed{border:1.5px dashed #333}
.panel--solid{border:1.5px solid #333}
.item{position:absolute;left:0;right:0;display:flex;flex-direction:column;align-items:center;text-align:center}
.item-title{display:flex;align-items:center;gap:6px;font-weight:700;font-size:9.5px;letter-spacing:.5px;color:var(--ink);margin-bottom:4px;white-space:nowrap}
.item-title::before,.item-title::after{content:"";width:14px;height:1.5px;background:var(--ink)}
.item-desc{font-size:6.6px;line-height:1.8;color:var(--text);padding:0 6px}
.item-desc b{font-weight:600;color:var(--ink)}
.legend{line-height:1.4;margin-top:6px}
.price{position:relative;margin-top:6px;width:80px;height:9px;border-radius:5px;background:var(--pill);color:#fff;font-size:6.5px;font-weight:700;line-height:9px;text-align:center}
.price::before,.price::after{content:"";position:absolute;top:4px;width:8px;height:1px;background:var(--pill)}
.price::before{left:-6px}.price::after{right:-6px}
.note{font-size:6.6px;color:var(--text)}
.brace{position:absolute}
</style>
</head>
<body>

<section class="sheet sheet--front">
  <div class="cover-photo" role="img" aria-label="Close-up photograph of golden toasted sandwiches piled on a white cloth"></div>
  <svg class="cover-diamond" width="756" height="534" viewBox="0 0 756 534">
    <polygon points="378,42 604,266 378,490 152,266" fill="none" stroke="#ffffff" stroke-width="2" opacity=".85"/>
    <polygon points="378,70 576,266 378,462 180,266" fill="#ffffff"/>
    <path d="M214,330 L184,336 L196,348 L186,360 L222,356 Z" fill="var(--blush)"/>
    <path d="M566,322 L598,316 L588,330 L600,342 L568,348 Z" fill="var(--blush)"/>
    <path d="M212,330 Q390,372 572,318 L572,346 Q390,402 212,358 Z" fill="var(--blush-soft)"/>
    <path id="ribbon-text" d="M222,352 Q390,392 566,336" fill="none"/>
    <text font-family="Oswald, sans-serif" font-size="17" fill="#ffffff" letter-spacing=".3">
      <textPath href="#ribbon-text" startOffset="50%" text-anchor="middle">PLEASE ORDER AND PAY AT THE COUNTER</textPath>
    </text>
  </svg>
  <div class="brand"><span class="brand-name">bloom &amp; crumb café</span><span class="brand-mark"></span></div>
</section>
<div class="side-label side-label--front">FRONT SIDE</div>

<section class="sheet sheet--back">
  <div class="back-frame"></div>

  <div class="panel panel--dashed" style="left:30px;top:42px;width:143px;height:452px">
    <div class="item" style="top:10px">
      <div class="item-title">TOAST</div>
      <p class="item-desc">sourdough / Brioche fruit loaf, with your choice of Ridgeway Preserve raspberry jam, Shoreline Honey, savoury spread, or Marlow's Peanut Butter (VGA) (GFA)</p>
      <div class="price">$8.50</div>
    </div>
    <div class="item" style="top:128px">
      <div class="item-title">FORAGE GRANOLA</div>
      <p class="item-desc">Almonds, macadamia nuts, sunflower seeds, pepitas, currants, pecan nuts, dates, cranberries and coconut. Spring fruits, Oat Lane almond milk.<br>(GF) (Vegan) (DF) (Paleo)</p>
      <div class="price">$15</div>
    </div>
    <div class="item" style="top:260px">
      <div class="item-title">WAFFLES</div>
      <p class="item-desc">Golden waffles, ice-cream, honeycomb, warm chocolate drizzle, strawberries (V)</p>
      <div class="price">$16</div>
    </div>
    <div class="item" style="top:356px">
      <div class="item-title">PERSIAN EGGS</div>
      <p class="item-desc">Free range poached eggs, walnut and pomegranate crumble, Persian fetta, roasted tomatoes, sourdough, sumac, watercress (V) (GFA)</p>
      <div class="price">$17</div>
    </div>
  </div>

  <svg class="brace" style="left:182px;top:42px" width="168" height="128" viewBox="0 0 168 128">
    <path d="M16,2 Q8,2 8,14 L8,52 Q8,63 1,64 Q8,65 8,76 L8,114 Q8,126 16,126" fill="none" stroke="#111" stroke-width="3"/>
    <path d="M152,2 Q160,2 160,14 L160,52 Q160,63 167,64 Q160,65 160,76 L160,114 Q160,126 152,126" fill="none" stroke="#111" stroke-width="3"/>
  </svg>
  <div class="panel" style="left:196px;top:42px;width:140px;height:190px">
    <div class="item" style="top:12px">
      <div class="item-title">BLOOM SMASH</div>
      <p class="item-desc">House-made pumpkin loaf, avocado, basil and pine nut pesto, baby tomato salsa, Hollis goat cheese, leaves, Sticky Fig Balsamic (V) (GFA) (VGA) DFA)</p>
      <div class="price">$20</div>
      <p class="note" style="margin-top:10px">Add free range egg</p>
      <div class="price">$2.5</div>
      <p class="note" style="margin-top:10px">Premium bacon</p>
      <div class="price">$4.5</div>
    </div>
  </div>
  <div class="panel panel--solid" style="left:193px;top:246px;width:143px;height:248px">
    <div class="item" style="top:12px">
      <div class="item-title">BRUSCHETTA</div>
      <p class="item-desc">Sautéed herby mushrooms, hummus, goat cheese, sourdough, Sticky Truffle Balsamic (V) (GFA)</p>
      <div class="price">$18</div>
    </div>
    <div class="item" style="top:105px">
      <div class="item-title">FRITTERS</div>
      <p class="item-desc">Sweet corn fritters, medley tomatoes, micro greens, poached egg, chilli, coriander, avocado and lime green goddess dressing (V)</p>
      <div class="price">$20</div>
      <p class="note" style="margin-top:16px">Add premium bacon</p>
      <div class="price" style="margin-top:8px">$4.5</div>
    </div>
  </div>

  <div class="panel panel--dashed" style="left:359px;top:42px;width:143px;height:452px">
    <div class="item" style="top:10px">
      <div class="item-title">BENNY TWO WAYS</div>
      <p class="item-desc">Premium bacon OR sautéed herby mushrooms, two free range poached eggs, spinach hollandaise, seeded sourdough (Mushroom version V)</p>
      <div class="price">$21</div>
    </div>
    <div class="item" style="top:114px">
      <div class="item-title">EGGS YOUR WAY</div>
      <p class="item-desc">Two free range eggs, poached, fried or scrambled, seeded sourdough, butter, if you wish (V) (GFA)</p>
      <div class="price">$13.50</div>
    </div>
    <div class="item" style="top:194px">
      <div class="item-title">ADDITIONS</div>
      <p class="item-desc">Bacon - Avocado $4.5 each<br>Hollis goat feta - Sautéed mushrooms $4 each<br>Slow roasted tomatoes $3.5 each<br>Hollandaise - Spinach - Free range egg $2.5 each<br>Tomato relish $2 each</p>
      <p class="item-desc legend">(V) vegetarian (VGA) Vegan Available (DF) Dairy Free (GF) Gluten Free (GFA) Gluten Free Available</p>
    </div>
    <div class="item" style="top:356px">
      <div class="item-title">LUNCH</div>
      <p class="item-desc">We offer lunch via our specials board to make the best use of the produce which comes our way. Simpler options are available in our display case. Please order and pay at the counter</p>
    </div>
  </div>

  <svg class="brace" style="left:514px;top:42px" width="216" height="128" viewBox="0 0 216 128">
    <path d="M18,2 Q10,2 10,14 L10,52 Q10,63 2,64 Q10,65 10,76 L10,114 Q10,126 18,126" fill="none" stroke="#111" stroke-width="3"/>
    <path d="M198,2 Q206,2 206,14 L206,52 Q206,63 214,64 Q206,65 206,76 L206,114 Q206,126 198,126" fill="none" stroke="#111" stroke-width="3"/>
  </svg>
  <div class="panel" style="left:532px;top:42px;width:180px;height:128px">
    <div class="item" style="top:12px">
      <div class="item-title">KIDS ONLY</div>
      <p class="item-desc"><b>Choco puffs</b> with milk $3.50<br><b>Berries</b> with natural yogurt $6<br><b>Croissant : Ham and cheese</b> $8.50<br><b>Toastie : Ham, cheese and tomato</b> $8.50<br><b>Little eggs : Scrambled eggs with buttered toast soldiers</b> $10<br><b>The lunch box :</b> Savoury spread &amp; cheese sandwich triangles, veggie sticks, dips, fruit &amp; yogurt cup in a cute cardboard lunch box $10</p>
    </div>
  </div>
  <div class="panel panel--dashed" style="left:526px;top:188px;width:200px;height:306px;border-top-style:solid">
    <div class="item" style="top:8px">
      <div class="item-title">DRINKS</div>
      <p class="item-desc">Coffee by Morning Bean Coffee, Harbour Bay &nbsp;Cup $4 &nbsp;Mug $4.5<br>(Not coffee) Hot chocolate, Chai latte (leaves, or powder), Dirty Chai</p>
      <p class="item-desc" style="margin-top:10px">Organic Leaf Tea &nbsp;&nbsp;&nbsp;&nbsp;&nbsp;&nbsp;&nbsp;&nbsp;&nbsp;$4.50<br>English Breakfast / Earl Grey / Camomile / Peppermint / Garden Blend / Liquorice Twist / Lemongrass &amp; Ginger / Green / Original Chai</p>
      <p class="item-desc" style="margin-top:10px">Organic orange juice (glass) $7<br>Milkshakes - Chocolate / Strawberry / Caramel /<br>Vanilla &nbsp;&nbsp;&nbsp;&nbsp;&nbsp;&nbsp;&nbsp;&nbsp;&nbsp;&nbsp;&nbsp;&nbsp;&nbsp;&nbsp;&nbsp;&nbsp;&nbsp;&nbsp;$6.50<br>Soy / Almond / Coconut + $1.5<br>Kids size $4</p>
      <p class="item-desc" style="margin-top:10px">Iced Drinks - Coffee / Chocolate / Mocha &nbsp;&nbsp;&nbsp;$7<br>Served with ice-cream &amp; whipped cream<br>Soy / Almond / Coconut + $1.5<br>Spider - Any of our fizzy flavours over ice cream (see fridge for selection) $7<br>Smoothies (please check counter for today's selection)</p>
    </div>
  </div>
</section>
<div class="side-label side-label--back">BACK SIDE</div>

</body>
</html>
```